Create a webpage for TradeRefundo

TradeRefundo.com is a new forex rebate site we wish to launch in parallel to our sister site payoutlegion.com

Were looking for a webpage with a modern, clean, corporate professional feel, that shows we are a reliable trustworthy company.

Our company offers commission to its registered users based on the volume of trading activity. Essentially they receive a payment everytime they transact irrespective of whether that trade makes money or loses money.

Blue and green are the colours we have decided on so but we are still open to other colour schemes as long as they have a refreshing clean and smart appearance.

Target Market(s)

Online retail forex traders

Industry/Entity Type

Trade

Requirements
Must have
• We are not looking for many pages but at a minimum the payout legion.com website can guide you.

Another site of interest;
CoinReturn Trades

```html
<!DOCTYPE html>
<html lang="en">
<head>
<meta charset="utf-8">
<title>TradeRefundo – Rebates on every trade</title>
<link href="https://fonts.googleapis.com/css2?family=Source+Sans+Pro:wght@300;400;600;700&display=swap" rel="stylesheet">
<style>
:root{
  --black:#0b0b0b;
  --green:#2ecc7e;
  --band:#4e9673;
  --band-light:#5a9f7d;
  --page:#f7f7f7;
  --white:#ffffff;
  --text:#555;
  --heading:#666;
  --icon:#8d8d8d;
  --arrow:#ececec;
  --menu:#2a2a2a;
}
*{box-sizing:border-box;margin:0;padding:0}
html,body{width:1200px;height:1200px;overflow:hidden}
body{position:relative;background:var(--page);font-family:"Source Sans Pro",Arial,sans-serif;color:var(--text)}
.abs{position:absolute}
.bar{left:0;width:1200px;height:45px;background:var(--black);display:flex;align-items:center}
.brand{position:absolute;left:88px;color:var(--white);font-weight:700;font-size:23px;letter-spacing:-.3px}
.nav{position:absolute;left:0;top:0;height:45px;width:1200px;list-style:none}
.nav li{position:absolute;top:15px;color:var(--white);font-size:13px;font-weight:600}
.user{left:992px;top:0;width:80px;height:45px;background:#2d2d2d;color:#ddd;font-size:13px;padding:13px 0 0 11px}
.avatar{left:1076px;top:4px;width:34px;height:36px;background:linear-gradient(#7a9cbf,#c7a48a)}
.dropdown{left:962px;top:45px;width:110px;height:92px;background:var(--menu);font-size:13px;color:#ddd}
.dropdown div{height:27px;line-height:27px;text-align:right;padding-right:9px;margin-top:3px}
.dropdown .on{background:var(--green);color:var(--white);font-weight:600}
.hero{left:0;top:45px;width:1200px;height:533px;background:linear-gradient(180deg,#9a9a9a 0%,#6f6f6f 30%,#3f4a3f 60%,#2a322b 100%)}
.hero h1{position:absolute;top:150px;width:1200px;text-align:center;color:var(--white);font-size:58px;font-weight:700;text-shadow:0 2px 4px rgba(0,0,0,.5)}
.btn{background:var(--green);color:var(--white);font-size:19px;font-weight:600;text-align:center;box-shadow:0 2px 3px rgba(0,0,0,.2)}
.hero .btn{position:absolute;left:460px;top:236px;width:282px;height:52px;line-height:52px}
.steps{left:86px;top:406px;width:1025px;height:224px;background:var(--white)}
.step{position:absolute;top:40px;width:200px;text-align:center;font-size:20px;color:#555}
.step svg{display:block;margin:0 auto 14px}
.band-wide{left:0;top:636px;width:1200px;height:133px;background:var(--band-light)}
.band{left:86px;top:630px;width:1026px;height:145px;background:var(--band);color:var(--white)}
.band p{position:absolute;left:25px;top:24px;width:730px;text-align:center;font-size:16.5px;line-height:23px}
.band .name{font-size:24px;font-weight:600}
.band .name-s{font-weight:600}
.band .btn{position:absolute;left:782px;top:47px;width:216px;height:52px;line-height:52px}
.content{left:86px;top:775px;width:1025px;height:380px;background:var(--white)}
.content h2{position:absolute;font-weight:300;font-size:29px;color:var(--heading)}
.broker{position:absolute;width:104px;height:36px;display:flex;align-items:center;gap:5px;font-size:13px;font-weight:700;color:#333}
.broker i{width:12px;height:12px;background:#2b6cb0;flex:none}
.blog-img{left:592px;top:91px;width:351px;height:127px;background:linear-gradient(135deg,#6d7f9a,#3a3026 60%,#5c6b3e)}
.blog-title{left:592px;top:225px;font-size:20px;color:#555}
.blog-text{left:592px;top:256px;width:355px;font-size:13.5px;line-height:18px;color:#666}
.more{left:882px;top:329px;font-size:11px;font-weight:600;color:#555;text-decoration:underline}
.social{position:absolute;top:1165px;width:24px;height:24px;border-radius:50%}
</style>
</head>
<body>

<header class="abs bar" style="top:0">
  <div class="brand">TradeRefundo</div>
  <ul class="nav">
    <li style="left:265px">FAQ</li><li style="left:326px">How it works</li><li style="left:425px">Compare brokers</li>
    <li style="left:559px">Products</li><li style="left:653px">Promotions</li><li style="left:775px">Blog</li><li style="left:859px">Contact Us</li>
  </ul>
</header>

<section class="abs hero" role="img" aria-label="Misty mountain valley landscape photo">
  <h1>Rebates on every trade. Simply.</h1>
  <div class="btn">JOIN NOW</div>
</section>

<div class="abs user">Hi, Jonas ▾</div>
<div class="abs avatar" role="img" aria-label="User avatar photo"></div>
<nav class="abs dropdown">
  <div>My account</div><div class="on">Profile</div><div>Logout</div>
</nav>

<section class="abs steps">
  <svg class="abs" style="left:240px;top:34px" width="150" height="148"><polygon points="0,50 54,50 54,0 150,74 54,148 54,98 0,98" fill="var(--arrow)"/></svg>
  <svg class="abs" style="left:656px;top:34px" width="150" height="148"><polygon points="0,50 54,50 54,0 150,74 54,148 54,98 0,98" fill="var(--arrow)"/></svg>

  <div class="step" style="left:34px">
    <svg width="100" height="100" viewBox="0 0 100 100">
      <rect x="2" y="22" width="60" height="42" rx="4" fill="var(--icon)"/>
      <circle cx="28" cy="46" r="12" fill="#fff"/><circle cx="28" cy="46" r="8" fill="var(--icon)"/>
      <circle cx="72" cy="42" r="30" fill="var(--icon)" stroke="#fff" stroke-width="4"/>
      <polygon points="72,22 90,42 80,42 80,58 64,58 64,42 54,42" fill="#fff"/>
    </svg>Create an account</div>
  <div class="step" style="left:413px">
    <svg width="100" height="100" viewBox="0 0 100 100">
      <path d="M20 40 A34 34 0 0 1 82 32" fill="none" stroke="var(--icon)" stroke-width="9"/>
      <path d="M80 60 A34 34 0 0 1 18 68" fill="none" stroke="var(--icon)" stroke-width="9"/>
      <polygon points="90,20 90,44 68,36" fill="var(--icon)"/><polygon points="10,80 10,56 32,64" fill="var(--icon)"/>
      <text x="50" y="68" text-anchor="middle" font-size="52" font-weight="700" fill="var(--icon)" font-family="Source Sans Pro,sans-serif">$</text>
    </svg>Trade as usuall</div>
  <div class="step" style="left:812px">
    <svg width="100" height="100" viewBox="0 0 100 100">
      <rect x="30" y="8" width="44" height="44" transform="rotate(45 52 30)" fill="none" stroke="var(--icon)" stroke-width="6"/>
      <text x="52" y="42" text-anchor="middle" font-size="30" font-weight="700" fill="var(--icon)" font-family="Source Sans Pro,sans-serif">$</text>
      <path d="M30 60 L50 78 L66 62" fill="none" stroke="var(--icon)" stroke-width="8"/>
      <rect x="34" y="86" width="30" height="10" fill="var(--icon)"/>
    </svg>Earn money</div>
</section>

<div class="abs band-wide"></div>
<section class="abs band">
  <p>With <span class="name">TradeRefundo</span> you can start making money on every forex, commodity or CFD trade you enter whether you are profitable or not! For seasoned forex traders, forex rebates are nothing new. For many of the new traders, forex rebates may be something that you have come across but not fully understood. Either way, by joining <span class="name-s">TradeRefundo</span> we can all benefit.</p>
  <div class="btn">JOIN NOW</div>
</section>

<section class="abs content">
  <h2 style="left:146px;top:36px">Forex Brokerage</h2>
  <h2 style="left:658px;top:35px">Latest from the blog</h2>

  <div class="broker" style="left:66px;top:107px"><i></i>Steelmark FX</div>
  <div class="broker" style="left:188px;top:107px"><i></i>Borealis FX</div>
  <div class="broker" style="left:326px;top:107px"><i></i>Simpla Trade</div>
  <div class="broker" style="left:70px;top:174px"><i></i>Quickmark FX</div>
  <div class="broker" style="left:188px;top:172px"><i></i>Emberline FX</div>
  <div class="broker" style="left:326px;top:169px"><i></i>Pipsphere</div>
  <div class="broker" style="left:66px;top:228px"><i></i>Quadra XP</div>
  <div class="broker" style="left:188px;top:227px"><i></i>Featherline</div>
  <div class="broker" style="left:326px;top:220px"><i></i>CurrencyHub</div>
  <div class="broker" style="left:66px;top:290px"><i></i>Clearpath FX</div>
  <div class="broker" style="left:188px;top:287px"><i></i>Openvale FX</div>
  <div class="broker" style="left:330px;top:295px"><i></i>Tickpoint</div>

  <div class="abs blog-img" role="img" aria-label="Bronze bull statue on a city street"></div>
  <div class="abs blog-title">Lorem ipsum dolor sit</div>
  <p class="abs blog-text">Nunc scelerisque ultrices arcu, vel cursus tortor tincidunt vitae. Aliquam erat volutpat. Vivamus auctor vulputate dui at euismod. Suspendisse consequat, dolor sit amet aliquam sollicitudin, est diam auctor ante, quis.</p>
  <div class="abs more">READ MORE</div>
</section>

<footer class="abs bar" style="top:1155px">
  <div class="brand">TradeRefundo</div>
  <ul class="nav">
    <li style="left:265px">FAQ</li><li style="left:326px">How it works</li><li style="left:425px">Compare brokers</li>
    <li style="left:559px">Products</li><li style="left:653px">Promotions</li><li style="left:775px">Blog</li><li style="left:859px">Contact Us</li>
  </ul>
</footer>
<span class="social" style="left:1017px;background:#5cb6e4" aria-label="Social link"></span>
<span class="social" style="left:1050px;background:#3a3a3a" aria-label="Social link"></span>
<span class="social" style="left:1082px;background:#4a72b8" aria-label="Social link"></span>

</body>
</html>
```